Stationery Design Project - Meridan-Vale

Business Cards
Size: 90mm x 55mm

Letterhead
Size: A4 - 210mm x 297mm

With Compliments Slip
Size: DL - 210mm x 99mm

Notepad
Size: 250mm x 140mm

Presentation Folder
Size: A4

Meridan-Vale
*Perth *Brisbane *Seoul *Hongkong

website: www.meridanvale.com.au (Currently live, but being replaced with new one)

Engineering and Technical recruitment company for the Mining, Oil & Gas, Construction & Engineering Sectors
Updates

Industry/Entity Type

Business

```html
<!DOCTYPE html>
<html lang="en">
<head>
<meta charset="utf-8">
<title>Meridan-Vale – DL Envelope</title>
<link rel="stylesheet" href="https://fonts.googleapis.com/css2?family=Open+Sans:wght@300;400;600;700&display=swap">
<style>
  :root {
    --bg: #e9eaec;
    --paper: #fbfbfc;
    --paper-edge: #dcdde0;
    --ink: #2a2d33;
    --navy: #1b2a6b;
    --blue-dark: #12307a;
    --blue-light: #2a9be0;
    --window: #eeeff1;
    --window-edge: #cfd1d5;
    --flap-line: #e1e2e5;
  }
  * { box-sizing: border-box; margin: 0; padding: 0; }
  html, body { width: 1200px; height: 960px; overflow: hidden; }
  body {
    background: var(--bg);
    font-family: "Open Sans", Arial, sans-serif;
    color: var(--ink);
    position: relative;
  }
  .envelope {
    position: absolute;
    width: 640px;
    height: 320px;
    background: var(--paper);
    border: 1px solid var(--paper-edge);
    box-shadow: 0 14px 30px rgba(0,0,0,0.12), 0 2px 4px rgba(0,0,0,0.08);
    overflow: hidden;
  }
  .envelope--back { left: 500px; top: 110px; }
  .envelope--front { left: 60px; top: 530px; }

  /* back */
  .flap { position: absolute; inset: 0; width: 100%; height: 100%; }
  .back-brand {
    position: absolute;
    left: 0; right: 0; top: 190px;
    display: flex;
    justify-content: center;
    align-items: center;
    gap: 12px;
  }
  .brand-dot {
    width: 38px; height: 38px;
    border-radius: 50%;
    background: var(--navy);
    flex: none;
  }
  .back-brand__web {
    font-size: 15px;
    font-weight: 600;
    letter-spacing: 1.5px;
    color: var(--navy);
  }

  /* front */
  .front-brand {
    position: absolute;
    left: 32px; top: 26px;
    display: flex;
    align-items: center;
    gap: 10px;
  }
  .front-brand .brand-dot { width: 30px; height: 30px; }
  .front-brand__name {
    font-size: 24px;
    font-weight: 300;
    letter-spacing: 1px;
    color: var(--navy);
  }
  .sender-address {
    position: absolute;
    left: 32px; top: 68px;
    font-size: 10.5px;
    line-height: 1.45;
    color: var(--ink);
  }
  .address-window {
    position: absolute;
    left: 32px; top: 110px;
    width: 250px; height: 100px;
    border-radius: 10px;
    background: var(--window);
    border: 1px solid var(--window-edge);
  }
  .accent-band {
    position: absolute;
    left: 0; bottom: 26px;
    width: 72%;
    height: 4px;
    background: linear-gradient(90deg, var(--blue-dark), var(--blue-light) 55%, var(--blue-dark));
  }
</style>
</head>
<body>

  <section class="envelope envelope--back" aria-label="Envelope back">
    <svg class="flap" viewBox="0 0 640 320" aria-hidden="true">
      <path d="M0 0 L0 150 Q0 165 15 168 L625 168 Q640 165 640 150 L640 0" fill="none" stroke="var(--flap-line)" stroke-width="1.5"/>
      <rect x="40" y="14" width="560" height="22" rx="4" fill="#f3f4f5" stroke="var(--flap-line)"/>
    </svg>
    <div class="back-brand">
      <span class="brand-dot"></span>
      <span class="back-brand__web">www.meridanvale.com.au</span>
    </div>
  </section>

  <section class="envelope envelope--front" aria-label="Envelope front">
    <div class="front-brand">
      <span class="brand-dot"></span>
      <span class="front-brand__name">Meridan-Vale</span>
    </div>
    <p class="sender-address">Level 4, 18 Harlow St, EASTBROOK<br>NSW 2190, Australia</p>
    <div class="address-window"></div>
    <div class="accent-band"></div>
  </section>

</body>
</html>
```